Business Card Design

An energy company designed around renewable energy and energy storage that focuses on providing its energy at points on the grid that reduce costs and add value to the system.

Industry/Entity Type

Business

Contact Information for Business Card

Martin Dellacroix
Executive Vice President
41 K ST NE
Washington, DC 20017
240-555-0187
mdellacroix@brightvaleenergy.example

```html
<!DOCTYPE html>
<html lang="en">
<head>
<meta charset="utf-8">
<title>Brightvale Energy – Business Card</title>
<link href="https://fonts.googleapis.com/css2?family=Quicksand:wght@400;500&family=Ubuntu:wght@400;500&display=swap" rel="stylesheet">
<style>
  :root {
    --backdrop: #2b2b2b;
    --card-light: #a9bb9c;
    --card-mid: #6c7f60;
    --card-dark: #3c4a36;
    --brand-green: #5cc43c;
    --text-light: #f3f5f0;
    --text-muted: #c9d2c2;
  }
  * { margin: 0; padding: 0; box-sizing: border-box; }
  html, body {
    width: 1200px; height: 800px; overflow: hidden;
    background: var(--backdrop);
  }
  .canvas {
    position: relative; width: 1200px; height: 800px;
    display: flex; align-items: center; justify-content: center;
  }
  .card {
    position: relative; width: 1050px; height: 600px;
    border-radius: 34px; overflow: hidden;
    box-shadow: 0 18px 40px rgba(0,0,0,0.5);
  }
  .card-backdrop {
    position: absolute; inset: 0;
    background: radial-gradient(ellipse 60% 65% at 52% 48%, var(--card-light) 0%, var(--card-mid) 45%, var(--card-dark) 100%);
  }
  .brand {
    position: absolute; left: 60px; top: 120px;
    display: flex; align-items: center; gap: 18px;
  }
  .brand-dot {
    width: 48px; height: 48px; border-radius: 50%;
    background: var(--brand-green); flex: none;
  }
  .brand-name {
    font-family: "Ubuntu", sans-serif; font-weight: 500;
    font-size: 50px; line-height: 1.05; color: var(--brand-green);
  }
  .identity {
    position: absolute; right: 60px; top: 62px; text-align: left;
  }
  .identity-name {
    font-family: "Ubuntu", sans-serif; font-weight: 500;
    font-size: 38px; color: var(--text-light); letter-spacing: 1px;
  }
  .identity-title {
    font-family: "Quicksand", sans-serif; font-weight: 400;
    font-size: 22px; color: var(--text-muted); letter-spacing: 1.5px; margin-top: 6px;
  }
  .contacts {
    position: absolute; right: 50px; bottom: 70px;
    list-style: none; display: flex; flex-direction: column; gap: 28px;
  }
  .contact-item {
    display: flex; align-items: center; justify-content: flex-end; gap: 20px;
    font-family: "Quicksand", sans-serif; font-weight: 500;
    font-size: 27px; color: var(--text-light); letter-spacing: 1px;
  }
  .contact-icon { width: 44px; height: 44px; flex: none; }
</style>
</head>
<body>
<main class="canvas">
  <section class="card" aria-label="Business card">
    <div class="card-backdrop" role="img" aria-label="Decorative sweeping curved light-line pattern on a soft green glow"></div>

    <div class="brand">
      <span class="brand-dot"></span>
      <span class="brand-name">Brightvale<br>Energy</span>
    </div>

    <div class="identity">
      <p class="identity-name">Martin Dellacroix</p>
      <p class="identity-title">Executive Vice President</p>
    </div>

    <ul class="contacts">
      <li class="contact-item">
        <span>240-555-0187</span>
        <svg class="contact-icon" viewBox="0 0 46 46" aria-label="Phone">
          <polygon points="23,2 42,13 42,33 23,44 4,33 4,13" fill="var(--brand-green)"/>
          <path d="M16 13 l5 0 l2 6 l-3 2 c1.5 3 3.5 5 6 6 l2 -3 l6 2 l0 5 c-10 1 -19 -8 -18 -18 z" fill="#fff"/>
        </svg>
      </li>
      <li class="contact-item">
        <span>mdellacroix@brightvaleenergy.example</span>
        <svg class="contact-icon" viewBox="0 0 46 46" aria-label="Email">
          <polygon points="23,2 42,13 42,33 23,44 4,33 4,13" fill="var(--brand-green)"/>
          <rect x="12" y="15" width="22" height="16" rx="1.5" fill="#fff"/>
          <path d="M12 16 L23 25 L34 16" fill="none" stroke="var(--brand-green)" stroke-width="2"/>
        </svg>
      </li>
      <li class="contact-item">
        <span>41 K ST NE&nbsp;&nbsp;Washington, DC 20017</span>
        <svg class="contact-icon" viewBox="0 0 46 46" aria-label="Location">
          <polygon points="23,2 42,13 42,33 23,44 4,33 4,13" fill="var(--brand-green)"/>
          <path d="M23 11 a8 8 0 0 1 8 8 c0 6 -8 15 -8 15 s-8 -9 -8 -15 a8 8 0 0 1 8 -8 z" fill="#fff"/>
          <circle cx="23" cy="19" r="3" fill="var(--brand-green)"/>
        </svg>
      </li>
    </ul>
  </section>
</main>
</body>
</html>
```